The Calm of Orchards New Book Cover Design Project

Book cover design . Paperback, ebook, and Vocara (derived from book cover) files/images required.
Book Title: The Calm of Orchards
Subtitle: Fewer Rusty Gates
Author: Dorian Halvey
Files: Ebook, Paperback (Brellix & Tolvent Press), Vocara sized image
File size & information to be provided once design is ready. Brellix paperback will be 5.25 x 8.
Completion date is flexible. Planning to publish in November.
Updates

Need extra days to review

Target Market(s)

Motorcycle owners

Font styles to use
Sans Serif

Requirements
Must have
• A generic looking motorcycle (samples attached). Thumbnail easily recognized as a motorcycle book.
Nice to have
• Open to all ideas but am favoring my idea: to emphasize the title lettering similar to (but not a copy of) other Calm books (examples attached), on a plain background. All books in the category have a motorcycle on the cover. Author name and subtitle do not have to be prominent. Rider optional..
Should not have
• Should not look like a biker romance or fantasy cover or look cartoonish. Motorcycle pic should be fairly generic (brand, style,).

```html
<!DOCTYPE html>
<html lang="en">
<head>
<meta charset="utf-8">
<title>The Calm of Orchards — Cover</title>
<link rel="stylesheet" href="https://fonts.googleapis.com/css2?family=Anton&family=Cormorant+Garamond:ital,wght@1,600&family=Jost:wght@400&display=swap">
<style>
  :root {
    --paper: #ffffff;
    --ink: #2f2f2f;
    --flame: #ff3d00;
    --bike-dark: #1c1c1e;
    --bike-chrome: #b9bcc0;
  }
  * { margin: 0; padding: 0; box-sizing: border-box; }
  html, body {
    width: 1200px;
    height: 624px;
    overflow: hidden;
    background: var(--paper);
  }
  .canvas {
    position: relative;
    width: 1200px;
    height: 624px;
    background: var(--paper);
  }
  .title {
    position: absolute;
    left: 0;
    top: 0;
    width: 1200px;
    height: 300px;
    font-weight: 400;
  }
  .title svg { display: block; }
  .title-word {
    font-family: "Anton", sans-serif;
  }
  .title-the, .title-rest { fill: var(--ink); }
  .title-calm { fill: var(--flame); }

  .motorcycle {
    position: absolute;
    left: 548px;
    top: 320px;
    width: 208px;
    height: 226px;
    border-radius: 40% 40% 30% 30% / 30% 30% 45% 45%;
    background: radial-gradient(ellipse at 55% 50%, var(--bike-dark) 0%, #3a3b3e 45%, var(--bike-chrome) 72%, rgba(255,255,255,0) 100%);
  }
  .subtitle-badge {
    position: absolute;
    left: 429px;
    top: 307px;
    width: 140px;
    height: 140px;
  }
  .subtitle-badge svg { position: absolute; inset: 0; }
  .subtitle-text {
    position: absolute;
    inset: 0;
    display: flex;
    align-items: center;
    justify-content: center;
    text-align: center;
    font-family: "Cormorant Garamond", serif;
    font-style: italic;
    font-weight: 600;
    font-size: 21px;
    line-height: 1;
    color: var(--paper);
    text-transform: uppercase;
  }
  .author {
    position: absolute;
    left: 400px;
    top: 576px;
    width: 400px;
    font-family: "Jost", sans-serif;
    font-weight: 400;
    font-size: 26px;
    line-height: 1;
    letter-spacing: 0.14em;
    color: var(--ink);
    text-align: center;
    text-transform: uppercase;
  }
</style>
</head>
<body>
  <main class="canvas">
    <h1 class="title">
      <svg viewBox="0 0 1200 300" width="1200" height="300">
        <title>The Calm of Orchards</title>
        <text class="title-word title-the" x="405" y="161" font-size="68" textLength="112" lengthAdjust="spacingAndGlyphs">THE</text>
        <text class="title-word title-calm" x="521" y="240" font-size="250" textLength="274" lengthAdjust="spacingAndGlyphs">calm</text>
        <text class="title-word title-rest" x="521" y="281" font-size="38" textLength="274" lengthAdjust="spacingAndGlyphs">OF ORCHARDS</text>
      </svg>
    </h1>

    <div class="motorcycle" role="img" aria-label="Photograph of a generic black classic motorcycle with chrome engine and spoked wheels, seen from the front three-quarter view"></div>

    <div class="subtitle-badge">
      <svg viewBox="0 0 144 144" width="140" height="140" aria-hidden="true">
        <polygon fill="var(--flame)" points="144,72 130.9,83.7 138.5,99.6 121.9,105.4 122.9,122.9 105.4,121.9 99.6,138.5 83.7,130.9 72,144 60.3,130.9 44.4,138.5 38.6,121.9 21.1,122.9 22.1,105.4 5.5,99.6 13.1,83.7 0,72 13.1,60.3 5.5,44.4 22.1,38.6 21.1,21.1 38.6,22.1 44.4,5.5 60.3,13.1 72,0 83.7,13.1 99.6,5.5 105.4,22.1 122.9,21.1 121.9,38.6 138.5,44.4 130.9,60.3"/>
      </svg>
      <p class="subtitle-text">Fewer<br>Rusty<br>Gates</p>
    </div>

    <p class="author">Dorian Halvey</p>
  </main>
</body>
</html>
```